" Duas amigas que dao consultoria de viagem desde a organizacao de todos os detalhes ate a criacao de roteiros personalizados para o passageiro. O objetivo é tornar a viagem mais produtiva e sem perda de tempos ou locais importantes deixados de serem visitados. "

```html
<!DOCTYPE html>
<html lang="pt-BR">
<head>
<meta charset="utf-8">
<title>Contato — Consultoria de Viagem</title>
<link rel="stylesheet" href="https://fonts.googleapis.com/css2?family=Open+Sans:wght@400;600;700&display=swap">
<style>
  :root {
    --page-bg: #f1f1f1;
    --panel: #ffffff;
    --ink: #444444;
    --ink-soft: #555555;
    --muted: #888888;
    --line: #d6d6d6;
    --field-border: #bdbdbd;
    --teal: #1b8ca4;
    --accent: #f2c617;
    --photo-sky: #c9d8df;
    --photo-rock: #6f7a63;
  }
  * { box-sizing: border-box; margin: 0; padding: 0; }
  html, body { width: 1200px; height: 1200px; overflow: hidden; }
  body {
    position: relative;
    background: var(--page-bg);
    font-family: "Open Sans", Arial, sans-serif;
    color: var(--ink);
  }
  .abs { position: absolute; }

  /* Main contact panel */
  .contact-panel { left: 89px; top: 0; width: 667px; height: 1037px; background: var(--panel); }
  .message-field { left: 149px; top: -4px; width: 542px; height: 81px; border: 2px solid var(--field-border); border-top: none; background: #fff; }
  .send-button {
    left: 149px; top: 108px; width: 230px; height: 55px;
    background: var(--teal); color: #fff; font-weight: 700; font-size: 21px;
    letter-spacing: 1px; display: flex; align-items: center; justify-content: center;
  }
  .section-title { left: 148px; font-weight: 700; font-size: 32px; color: var(--ink); white-space: nowrap; }
  .contact-line { left: 149px; display: flex; align-items: center; gap: 20px; font-size: 27px; color: var(--ink-soft); white-space: nowrap; }
  .contact-line svg { width: 30px; height: 30px; flex: none; }
  .social-list { left: 139px; top: 535px; display: flex; gap: 16px; }
  .social-dot { width: 59px; height: 59px; border: 2px solid #dcdcdc; border-radius: 50%; }

  /* Sidebar widgets */
  .widget { left: 814px; width: 297px; background: var(--panel); }
  .widget-title {
    position: absolute; left: 16px; width: 257px; font-size: 13px; font-weight: 600;
    color: var(--ink); padding-bottom: 6px; border-bottom: 3px solid var(--accent);
  }
  .post { left: 16px; display: flex; gap: 12px; }
  .post-thumb {
    width: 111px; height: 84px; flex: none;
    background: linear-gradient(180deg, var(--photo-sky) 0%, #b5c6cc 45%, var(--photo-rock) 70%, #5b6450 100%);
  }
  .post-title { font-weight: 700; font-size: 19px; line-height: 20px; color: #333; width: 130px; }
  .post-date { font-size: 10px; color: var(--muted); margin-top: 6px; }
  .tag {
    position: absolute; height: 29px; border: 1px solid #c9c9c9; font-size: 11px; color: var(--ink-soft);
    display: flex; align-items: center; justify-content: center; white-space: nowrap;
  }
  .archive-item { position: absolute; display: flex; align-items: center; gap: 7px; font-size: 16px; color: var(--ink-soft); white-space: nowrap; }
  .archive-item::before { content: ""; border-left: 7px solid #333; border-top: 5px solid transparent; border-bottom: 5px solid transparent; }
</style>
</head>
<body>
  <section class="abs contact-panel"></section>
  <div class="abs message-field"></div>
  <div class="abs send-button">ENVIAR</div>

  <h2 class="abs section-title" style="top:274px;">Ligue ou mande um email</h2>
  <div class="abs contact-line" style="top:340px;">
    <svg viewBox="0 0 24 24" aria-hidden="true"><path fill="#f2c617" d="M6.6 10.8a15.1 15.1 0 0 0 6.6 6.6l2.2-2.2c.3-.3.7-.4 1-.2 1.1.4 2.3.6 3.6.6.6 0 1 .4 1 1V20c0 .6-.4 1-1 1A17 17 0 0 1 3 4c0-.6.4-1 1-1h3.5c.6 0 1 .4 1 1 0 1.3.2 2.5.6 3.6.1.3 0 .7-.2 1z"/></svg>
    <span>(00) 0000-0000 / (00) 9 9999-9999</span>
  </div>
  <div class="abs contact-line" style="top:390px;">
    <svg viewBox="0 0 24 24" aria-hidden="true"><rect x="2" y="5" width="20" height="14" fill="#f2c617"/><path d="M2 5l10 8 10-8" fill="none" stroke="#fff" stroke-width="1.6"/></svg>
    <span>email@email.com.br</span>
  </div>

  <h2 class="abs section-title" style="top:462px;">Contate-me pelas Redes Sociais</h2>
  <div class="abs social-list" aria-label="Redes sociais">
    <span class="social-dot"></span><span class="social-dot"></span><span class="social-dot"></span>
    <span class="social-dot"></span><span class="social-dot"></span><span class="social-dot"></span>
    <span class="social-dot"></span>
  </div>

  <!-- Popular posts -->
  <aside class="abs widget" style="top:34px;height:643px;">
    <h3 class="widget-title" style="top:20px;">POSTS MAIS POPULARES</h3>
  </aside>
  <article class="abs post" style="left:830px;top:103px;"><div class="post-thumb" role="img" aria-label="Foto de viajante no alto de uma montanha"></div><div><p class="post-title">O título da notí-cia será exibido aqui</p><p class="post-date">15/06/2017</p></div></article>
  <article class="abs post" style="left:830px;top:213px;"><div class="post-thumb" role="img" aria-label="Foto de viajante no alto de uma montanha"></div><div><p class="post-title">O título da notí-cia será exibido aqui</p><p class="post-date">15/06/2017</p></div></article>
  <article class="abs post" style="left:830px;top:323px;"><div class="post-thumb" role="img" aria-label="Foto de viajante no alto de uma montanha"></div><div><p class="post-title">O título da notí-cia será exibido aqui</p><p class="post-date">15/06/2017</p></div></article>
  <article class="abs post" style="left:830px;top:434px;"><div class="post-thumb" role="img" aria-label="Foto de viajante no alto de uma montanha"></div><div><p class="post-title">O título da notí-cia será exibido aqui</p><p class="post-date">15/06/2017</p></div></article>
  <article class="abs post" style="left:830px;top:547px;"><div class="post-thumb" role="img" aria-label="Foto de viajante no alto de uma montanha"></div><div><p class="post-title">O título da notí-cia será exibido aqui</p><p class="post-date">15/06/2017</p></div></article>

  <!-- Tags -->
  <aside class="abs widget" style="top:713px;height:283px;">
    <h3 class="widget-title" style="top:20px;">TAGS</h3>
    <span class="tag" style="left:19px;top:65px;width:53px;">Dicas</span>
    <span class="tag" style="left:81px;top:65px;width:115px;">Turismo Nacional</span>
    <span class="tag" style="left:206px;top:65px;width:74px;">Férias</span>
    <span class="tag" style="left:19px;top:103px;width:132px;">Turismo Internacional</span>
    <span class="tag" style="left:163px;top:103px;width:74px;">Roteiros</span>
  </aside>

  <!-- Archive -->
  <aside class="abs widget" style="top:1037px;height:200px;">
    <h3 class="widget-title" style="top:18px;">ARQUIVO</h3>
    <span class="archive-item" style="left:20px;top:63px;">2017 (10)</span>
    <span class="archive-item" style="left:40px;top:85px;font-size:14px;">Janeiro (02)</span>
    <span class="archive-item" style="left:40px;top:104px;font-size:14px;">Fevereiro (02)</span>
    <span class="archive-item" style="left:40px;top:123px;font-size:14px;">Março (02)</span>
    <span class="archive-item" style="left:20px;top:152px;">2016</span>
  </aside>
</body>
</html>
```